Brightwater Health Partners, LLC Business Card update!

would like a classier business card. Our cards currently just have our logo and contact information. Need better use of color and creativity
Logo attached.

Target Market(s)

Potential clients, contacts, existing clients. We are a consulting company

Industry/Entity Type

Business

Contact Information for Business Card

We like our colors but just have a boring card with our logo and a white background. I want something that stands out.

Colors
ec1f27
757575

Requirements
Must have
• Color to stay consistent. Logo provided
Nice to have
• Just better use of color/ design

```html
<!DOCTYPE html>
<html lang="en">
<head>
<meta charset="utf-8">
<title>Brightwater Health Partners – Business Card</title>
<link rel="stylesheet" href="https://fonts.googleapis.com/css2?family=Crimson+Pro:ital,wght@0,400;1,400&family=Raleway:wght@300&display=swap">
<style>
  :root {
    --brand-red: #b80202;
    --brand-grey: #757575;
    --card-light: #dcdcdc;
    --card-mid: #cfcfcf;
    --ink-name: #454859;
    --ink-contact: #3a3a3a;
    --frame: #ffffff;
  }
  * { margin: 0; padding: 0; box-sizing: border-box; }
  html, body {
    width: 1200px;
    height: 685px;
    overflow: hidden;
    background: #ffffff;
  }
  .card {
    position: relative;
    width: 1200px;
    height: 685px;
    overflow: hidden;
    background: linear-gradient(100deg, var(--card-light) 0%, #d6d6d6 45%, var(--card-mid) 100%);
    font-family: "Crimson Pro", Georgia, serif;
  }
  .card-frame {
    position: absolute;
    inset: 5px;
    border: 1px solid var(--frame);
    pointer-events: none;
  }
  .brand-band {
    position: absolute;
    left: 0;
    top: 0;
    width: 988px;
    height: 224px;
    background: var(--brand-red);
    border-right: 1px solid #e8e8e8;
    border-bottom: 1px solid #e8e8e8;
  }
  .brand-mark {
    position: absolute;
    left: 46px;
    top: 52px;
    width: 124px;
    height: 124px;
  }
  .brand-name {
    position: absolute;
    left: 200px;
    top: 34px;
    width: 640px;
    font-size: 62px;
    line-height: 72px;
    font-weight: 400;
    color: var(--brand-grey);
  }
  .web-address {
    position: absolute;
    left: 1148px;
    top: 18px;
    width: 32px;
    height: 376px;
    writing-mode: vertical-rl;
    font-family: "Raleway", Arial, sans-serif;
    font-weight: 300;
    font-size: 25px;
    letter-spacing: 3px;
    color: #ffffff;
    text-align: center;
  }
  .person {
    position: absolute;
    left: 104px;
    top: 312px;
    width: 424px;
    text-align: right;
    color: var(--ink-name);
  }
  .person-name {
    font-size: 60px;
    line-height: 64px;
    font-weight: 400;
    letter-spacing: 1px;
    text-align: left;
  }
  .person-title {
    font-size: 44px;
    line-height: 50px;
    font-style: italic;
    font-variant: small-caps;
    letter-spacing: 1px;
  }
  .contact-line {
    position: absolute;
    left: 0;
    right: 0;
    top: 606px;
    text-align: center;
    font-size: 30px;
    color: var(--ink-contact);
    font-variant-numeric: oldstyle-nums;
    white-space: nowrap;
  }
  .contact-line .sep { padding: 0 3px; }
</style>
</head>
<body>
<main class="card">
  <section class="brand-band">
    <svg class="brand-mark" viewBox="0 0 124 124" aria-hidden="true">
      <circle cx="62" cy="62" r="48" fill="none" stroke="#757575" stroke-width="8"/>
    </svg>
    <h1 class="brand-name">Brightwater Health Partners</h1>
  </section>

  <p class="web-address">www.brightwaterhp.com</p>

  <div class="person">
    <h2 class="person-name">DANIEL HART</h2>
    <p class="person-title">Sales Director</p>
  </div>

  <p class="contact-line"><span class="sep">|</span>+61 02 4781 2093<span class="sep">|</span>+ 61 0 412 508 346<span class="sep">|</span>email: d.hart@bwhp.com<span class="sep">|</span>14 Harbour Rd., NSW 2000<span class="sep">|</span></p>

  <div class="card-frame"></div>
</main>
</body>
</html>
```